Hockey Youth Club - Complete HP Design

I need a complete homepage design for a new youth hockey club. There are already some elements that can be used. For more information, please visit this products webpage. This site is currently unavailable for purchase at this time (Current) -) Team (Players, Coaches, Crew) -) Club (Philiosophy , Rules, Management Board, ....) -) Partners (Sponsors, Partners, ...)) Contact (Contact details, Callback Button) -) Shop (in the beginning view of products - further planned as online shop ) -) .... probably 2-3 more -) Footer with social media info, ..... Homepages from other youth hockey clubs (ex. Www.plo. At - this is what I am looking for in my life - BUT we dont want to copy them !!! Im interested in new and innovative designs.
Updates

Project Deadline Extended
Reason: Too much Wordpress - no innovation - please offer more designs in dark concept. At the moment the design is too decent - we are looking for sporty, active and fresh design. Thank you

Target Market(s)

Youth Hockey Players Parents

Industry/Entity Type

Club

Number of Pages Required

5+ page

Colors
fbed38
9d9d9d
1b1b1b
f5f5f5
ffffff

Requirements
Must have
• Clearline, modern design,
Nice to have
• Flashing elements (maybe the scratches fading in ...)
Should not have
• chaos

```html
<!DOCTYPE html>
<html lang="en">
<head>
<meta charset="utf-8">
<title>Blades Youth Hockey Club</title>
<link href="https://fonts.googleapis.com/css2?family=Khand:wght@500;600;700&family=Open+Sans:wght@400;600;700&display=swap" rel="stylesheet">
<style>
:root{
  --yellow:#fbed38;
  --gold:#f5c400;
  --grey:#9d9d9d;
  --dark:#1b1b1b;
  --card:#2b2b2b;
  --light:#f5f5f5;
  --white:#ffffff;
  --sky:#6cbbe6;
  --head:"Khand", sans-serif;
  --body:"Open Sans", sans-serif;
}
*{margin:0;padding:0;box-sizing:border-box}
html,body{width:1200px;height:3082px;overflow:hidden}
body{position:relative;background:var(--white);font-family:var(--body);color:var(--dark)}
.abs{position:absolute}

/* header */
.site-logo{left:106px;top:14px;font:700 38px/1 var(--head);color:var(--gold);letter-spacing:2px;display:flex;align-items:center;gap:10px;z-index:5}
.site-logo .mark{width:26px;height:26px;border-radius:50%;background:var(--gold)}
.nav-band{left:650px;top:0;width:550px;height:80px;z-index:4}
.nav-link{top:12px;font:600 13px/1 var(--head);color:var(--yellow);text-decoration:none;letter-spacing:1px;z-index:5}
.login-btn{left:1091px;top:6px;width:66px;height:25px;border:1.5px solid var(--yellow);color:var(--yellow);font:600 13px/22px var(--head);text-align:center;letter-spacing:1px;z-index:5}

/* hero */
.hero{left:0;top:0;width:1200px;height:780px;
  background:
    linear-gradient(100deg,rgba(40,40,40,.0) 0%,rgba(40,40,40,.0) 8%,rgba(55,55,55,.45) 18%,rgba(55,55,55,.45) 40%,rgba(40,40,40,0) 52%),
    radial-gradient(ellipse 70% 60% at 45% 40%,#e2e2e2 0%,#b4b4b4 45%,#7c7c7c 80%,#5e5e5e 100%);}
.hero-title{left:580px;top:338px;font-family:var(--head);font-weight:700;color:var(--dark);line-height:.82}
.hero-title .big{font-size:132px;display:block;letter-spacing:-2px}
.hero-title .the{font-size:56px;letter-spacing:0}
.hero-title .game{color:var(--gold)}
.hero-title .changers{font-size:80px;letter-spacing:-1px;margin-top:10px}

/* team */
.team{left:0;top:700px;width:1200px;height:800px;background:linear-gradient(180deg,#14161e 0%,#2a2f45 40%,#4a5478 75%,#8a90ad 100%)}
.section-title{font:700 34px/1 var(--head);letter-spacing:14px;text-align:center;width:1200px;left:0}
.team-title{top:836px;color:var(--gold)}
.event-photo{background:linear-gradient(160deg,#e8edf3 0%,#b7c2cf 45%,#c2463a 70%,#8a2a22 100%)}
.event-card{overflow:hidden}
.event-body{background:var(--yellow);position:absolute;left:0;bottom:0;width:100%}
.event-date{font:700 68px/.8 var(--head);color:var(--white)}
.event-heading{font:700 17px/1.1 var(--head);color:var(--dark)}
.event-text{font:600 10.5px/1.35 var(--body);color:var(--dark);margin-top:3px}
.panel{background:rgba(40,40,40,.82);padding:10px 14px;color:var(--white)}
.panel .event-heading{color:var(--yellow)}
.panel .event-text{color:var(--white)}
.next-arrow{left:1072px;top:1050px}

/* shop */
.shop-title{left:522px;top:1597px;width:158px;height:47px;border:2px solid var(--dark);font:700 24px/43px var(--head);letter-spacing:9px;text-align:center;padding-left:8px}
.product{background:var(--card)}
.product.light{background:var(--yellow)}
.product-img{background:linear-gradient(160deg,#ffffff 0%,#e3e3e3 60%,#c9c9c9 100%)}
.glove-img{background:linear-gradient(150deg,#ffffff 10%,#c02a2a 45%,#1b1b1b 80%,#ffffff 95%)}
.product-name{font:700 30px/1 var(--head);color:var(--gold)}
.product.light .product-name{font-size:22px;color:var(--dark)}
.price{font:700 30px/1 var(--head);color:var(--gold);text-align:right}
.product.light .price{font-size:22px;color:var(--dark)}
.cart{font:700 11px/1 var(--body);color:var(--white);text-align:right}
.product.light .cart{font-size:8px;color:var(--dark)}
.details{font:600 9px/1 var(--body);color:var(--white)}
.product.light .details{font-size:7px;color:var(--dark)}
.view-all{left:545px;top:2151px;width:110px;height:27px;background:var(--card);color:var(--white);font:700 12px/27px var(--head);letter-spacing:4px;text-align:center}

/* follow */
.follow{left:0;top:2260px;width:1200px;height:540px;background:radial-gradient(ellipse at 60% 45%,#c8c8c8 0%,#dedede 40%,#f5f5f5 80%)}
.follow-title{top:2338px;color:var(--dark);font-size:28px}
.label{font:700 15px/1 var(--head);letter-spacing:6px;color:var(--dark)}
.fb-widget{left:290px;top:2456px;width:279px;height:185px;background:var(--white);box-shadow:0 1px 4px rgba(0,0,0,.2)}
.fb-cover{left:0;top:0;width:279px;height:108px;background:linear-gradient(120deg,#7a5a3a,#c08a52,#3c4c6e)}
.fb-name{left:10px;top:8px;display:flex;align-items:center;gap:6px;font:700 14px/1 var(--head);color:var(--white)}
.fb-name .sq{width:18px;height:18px;background:var(--white)}
.fb-btn{background:var(--light);border:1px solid #ccc;font:600 9px/16px var(--body);padding:0 6px;color:#333}
.fb-foot{left:10px;top:122px;font:400 9px/1 var(--body);color:#555}
.fb-faces{left:10px;top:138px;display:flex;gap:4px}
.fb-faces span{width:22px;height:22px;background:#bbb}
.tw-box{left:639px;top:2456px;width:255px;height:181px;background:var(--sky);padding:36px 28px 0}
.tw-box .event-heading{font:600 12px/1.35 var(--body);color:var(--dark)}
.tw-box .event-text{font:400 12px/1.35 var(--body);text-align:justify}
.tw-btn{margin-top:18px;display:inline-block;background:var(--yellow);font:600 12px/30px var(--head);padding:0 22px;color:var(--dark)}

/* footer */
.site-footer{left:0;top:2800px;width:1200px;height:282px;background:var(--white)}
.foot-col{text-align:center;font:700 13px/25px var(--head);letter-spacing:2px;color:var(--dark)}
.foot-col .accent{color:var(--gold);letter-spacing:5px}
.foot-divider{width:2px;height:126px;background:var(--dark);top:2840px}
</style>
</head>
<body>

<!-- hero -->
<section class="hero abs" role="img" aria-label="Black and white photo of a youth hockey player skating with a stick across scratched ice"></section>
<svg class="nav-band abs" viewBox="0 0 550 80" aria-hidden="true">
  <path d="M8 0H550V40C440 42 300 52 12 74Z" fill="#2f2f2f"/>
  <path d="M12 74C300 52 440 42 550 40" stroke="#fbed38" stroke-width="3" fill="none"/>
</svg>
<div class="site-logo abs"><span class="mark"></span>BLADES</div>
<nav>
  <a class="nav-link abs" style="left:711px" href="#">TEAM</a>
  <a class="nav-link abs" style="left:787px" href="#">CLUB</a>
  <a class="nav-link abs" style="left:849px" href="#">PARTNERS</a>
  <a class="nav-link abs" style="left:929px" href="#">CONTACT</a>
  <a class="nav-link abs" style="left:1011px" href="#">SHOP</a>
</nav>
<div class="login-btn abs">LOGIN</div>
<h1 class="hero-title abs">
  <span class="big">WE<span class="the">THE</span></span>
  <span class="big game">GAME</span>
  <span class="big changers">CHANGERS</span>
</h1>

<!-- team -->
<section class="team abs" role="img" aria-label="Photo of an indoor hockey arena with a crowd"></section>
<svg class="abs" style="left:0;top:660px" width="1200" height="110" viewBox="0 0 1200 110" aria-hidden="true">
  <path d="M0 0H1200V40C1000 110 800 20 600 60C400 100 200 40 0 90Z" fill="#6f6f6f"/>
</svg>
<h2 class="section-title team-title abs">OUR TEAM</h2>

<article class="event-card abs" style="left:105px;top:918px;width:376px;height:340px">
  <div class="event-photo abs" style="left:0;top:0;width:376px;height:214px" role="img" aria-label="Photo of young players in red jerseys on the ice"></div>
  <div class="event-body" style="height:126px;padding:12px 14px;display:flex;gap:16px">
    <div class="event-date">15<br>Jun</div>
    <div><div class="event-heading">Lorem ipsum dolor sit amet</div>
    <p class="event-text">Consectetur adipiscing elit. Mauris lobortis ex quis augue laoreet, et scelerisque justo mollis. Nam convallis dapibus dui, ultricies vestibulum velit tempus in. Phasellus porta massa sit amet eros ultricies, maximus.</p></div>
  </div>
</article>

<article class="event-card abs" style="left:503px;top:918px;width:255px;height:340px">
  <div class="event-photo abs" style="left:0;top:0;width:255px;height:340px;background:linear-gradient(180deg,#3b4258,#6b7490 50%,#9aa2bb)" role="img" aria-label="Photo of a player on the ice"></div>
  <div class="panel abs" style="left:8px;top:56px;width:240px">
    <div class="event-heading">Lorem ipsum dolor sit amet</div>
    <p class="event-text">Consectetur adipiscing elit. Mauris lobortis ex quis augue laoreet, et scelerisque justo mollis. Nam convallis dapibus dui, ultricies vestibulum velit tempus in. Phasellus porta massa sit amet</p>
  </div>
  <div class="panel abs" style="left:8px;top:178px;width:240px;height:150px;padding-top:40px">
    <div class="event-heading">Lorem ipsum dolor sit amet</div>
    <p class="event-text">Consectetur adipiscing elit. Mauris lobortis ex quis augue laoreet, et scelerisque justo mollis. Nam convallis dapibus dui, ultricies vestibulum velit tempus in. Phasellus porta massa sit amet</p>
  </div>
</article>

<article class="event-card abs" style="left:770px;top:918px;width:258px;height:340px">
  <div class="event-photo abs" style="left:0;top:0;width:258px;height:214px;background:linear-gradient(150deg,#d9e2ea 0%,#b8c6d4 40%,#e05a2a 70%,#9c3418 100%)" role="img" aria-label="Photo of a player in an orange jersey skating"></div>
  <div class="event-date abs" style="left:18px;top:70px;color:var(--dark);font-size:62px">05<br>Jun</div>
  <div class="event-body" style="height:126px;padding:16px 18px">
    <div class="event-heading">Lorem ipsum dolor sit amet</div>
    <p class="event-text">Consectetur adipiscing elit. Mauris lobortis ex quis augue laoreet, et scelerisque justo mollis. Nam convallis dapibus dui, ultricies vestibulum velit tempus in. Phasellus porta massa sit amet eros</p>
  </div>
</article>

<svg class="next-arrow abs" width="28" height="70" viewBox="0 0 28 70" aria-label="Next">
  <path d="M4 4L24 35L4 66" stroke="#ffffff" stroke-width="5" fill="none"/>
</svg>

<svg class="abs" style="left:0;top:1300px" width="1200" height="210" viewBox="0 0 1200 210" aria-hidden="true">
  <path d="M0 90C120 40 200 150 330 110C460 70 520 160 660 120C800 80 880 150 1000 100C1090 70 1150 110 1200 90V210H0Z" fill="#ffffff"/>
</svg>

<!-- shop -->
<h2 class="shop-title abs">SHOP</h2>

<article class="product abs" style="left:166px;top:1691px;width:298px;height:438px">
  <div class="product-img abs" style="left:12px;top:12px;width:274px;height:286px" role="img" aria-label="Photo of a white race T-shirt with a flag print"></div>
  <div class="product-name abs" style="left:20px;top:320px">SEASON 11<br>TSHIRT</div>
  <div class="price abs" style="right:28px;top:340px">$20</div>
  <div class="cart abs" style="right:28px;top:376px">ADD TO CART</div>
  <div class="details abs" style="left:26px;top:388px">View Details</div>
</article>

<article class="product light abs" style="left:495px;top:1691px;width:195px;height:209px">
  <div class="glove-img abs" style="left:12px;top:12px;width:171px;height:136px" role="img" aria-label="Photo of a pair of red and black hockey gloves"></div>
  <div class="product-name abs" style="left:12px;top:164px">GLOVES</div>
  <div class="price abs" style="right:14px;top:160px">$20</div>
  <div class="details abs" style="left:12px;top:186px">View Details</div>
  <div class="cart abs" style="right:14px;top:186px">ADD TO CART</div>
</article>

<article class="product light abs" style="left:495px;top:1915px;width:195px;height:214px">
  <div class="glove-img abs" style="left:12px;top:12px;width:171px;height:140px" role="img" aria-label="Photo of a pair of red and black hockey gloves"></div>
  <div class="product-name abs" style="left:12px;top:168px">GLOVES</div>
  <div class="price abs" style="right:14px;top:164px">$20</div>
  <div class="details abs" style="left:12px;top:190px">View Details</div>
  <div class="cart abs" style="right:14px;top:190px">ADD TO CART</div>
</article>

<article class="product abs" style="left:727px;top:1691px;width:309px;height:438px">
  <div class="product-img abs" style="left:12px;top:12px;width:285px;height:280px" role="img" aria-label="Photo of a white T-shirt with a sailboat print"></div>
  <div class="product-name abs" style="left:24px;top:322px">SEASON 03<br>TSHIRT</div>
  <div class="price abs" style="right:26px;top:344px">$20</div>
  <div class="cart abs" style="right:26px;top:380px">ADD TO CART</div>
  <div class="details abs" style="left:30px;top:394px">View Details</div>
</article>

<div class="view-all abs">VIEW ALL</div>

<!-- follow -->
<section class="follow abs" role="img" aria-label="Faded photo of a hockey player in a white jersey on ice"></section>
<svg class="abs" style="left:0;top:2250px" width="1200" height="80" viewBox="0 0 1200 80" aria-hidden="true">
  <path d="M0 0H1200V30C1050 70 950 20 800 50C650 80 520 30 380 55C240 80 120 30 0 60Z" fill="#ffffff"/>
</svg>
<svg class="abs" style="left:0;top:2700px" width="1200" height="110" viewBox="0 0 1200 110" aria-hidden="true">
  <path d="M0 60C150 20 260 90 420 60C580 30 700 90 860 55C1000 25 1100 70 1200 50V110H0Z" fill="#ffffff"/>
</svg>
<h2 class="section-title follow-title abs">FOLLOW US</h2>

<div class="label abs" style="left:302px;top:2432px">FACELINK</div>
<div class="label abs" style="left:648px;top:2432px">CHIRPER</div>

<div class="fb-widget abs">
  <div class="fb-cover abs" role="img" aria-label="Cover photo of club members at a table"></div>
  <div class="fb-name abs"><span class="sq"></span>Facelink<br>Club page</div>
  <div class="fb-btn abs" style="left:10px;top:84px">Like Page</div>
  <div class="fb-btn abs" style="right:10px;top:84px">Share</div>
  <div class="fb-foot abs">Be the first of your friends to like this.</div>
  <div class="fb-faces abs"><span></span><span></span><span></span><span></span><span></span><span></span><span></span><span></span></div>
</div>

<div class="tw-box abs">
  <div class="event-heading">Lorem ipsum dolor sit amet</div>
  <p class="event-text">Consectetur adipiscing elit. Mauris lobortis ex quis augue laoreet, et scelerisque justo mollis. Nam convallis dapibus dui, ultricies</p>
  <span class="tw-btn">TO CHIRPER</span>
</div>
<svg class="abs" style="left:644px;top:2650px" width="12" height="12" viewBox="0 0 12 12" aria-hidden="true"><circle cx="6" cy="6" r="5" fill="#6cbbe6"/></svg>

<!-- footer -->
<footer class="site-footer abs"></footer>
<nav class="foot-col abs" style="left:187px;top:2844px;width:120px">HOME<br>TEAM<br>CLUB<br>PARTNERS<br>SHOP<br>CONTACT</nav>
<div class="foot-divider abs" style="left:358px"></div>
<div class="foot-col abs" style="left:420px;top:2844px;width:166px"><span class="accent">FOLLOW US</span><br>FACELINK &nbsp;-<br>CHIRPER &nbsp;-</div>
<div class="foot-divider abs" style="left:663px"></div>
<address class="foot-col abs" style="left:752px;top:2844px;width:160px;font-style:normal"><span class="accent">ADDRESS</span><br>D.NO-123,<br>STREET,<br>CITY,<br>COUNTRY-12345</address>
<div class="foot-col abs" style="left:972px;top:2844px;width:180px">CONTACT<br>PHONE:123-456-789<br>EMAIL: MAIL@COM</div>

</body>
</html>
```